Corporate identity and pre-opening design for a brand new Casino

Dear designers!

We need a design for the pre-opening ad campaign of our brand new casino called "Velvorn Casino" and planned to open soon.
It is situated in "Merisk Lodge Tarvena" – a 4-star luxury and business hotel, located in the city of Plovdiv, Bulgaria.
Our vision of the project is bold, but stylish and elegant. We desire to see uniqueness by all means.
Our slogan is “So many ways to have fun”.
We need a design for our ad campaign for ex. billbord 8m x 4m. We expect your elegant and creative designs. We are trying to avoid the conventional, but at the same time we do not want to be too extravagant.

Thank you and good luck!

Requirements
Should not have
• dices

```html
<!DOCTYPE html>
<html lang="en">
<head>
<meta charset="utf-8">
<title>Velvorn Casino – Coming Soon Billboard</title>
<link rel="stylesheet" href="https://fonts.googleapis.com/css2?family=Arimo:wght@700&family=Marcellus&display=swap">
<style>
  :root {
    --page-bg: #e6e8eb;
    --panel-orange: #f7991f;
    --panel-white: #ffffff;
    --ink: #0d0d0d;
    --divider: #3a3a3a;
    --pattern-deep: #e63b24;
    --pattern-mid: #f26522;
    --pattern-light: #f7941d;
  }
  * { margin: 0; padding: 0; box-sizing: border-box; }
  html, body {
    width: 1200px;
    height: 704px;
    overflow: hidden;
    background: var(--page-bg);
  }
  .billboard {
    position: absolute;
    left: 30px;
    top: 62px;
    width: 1140px;
    height: 580px;
    display: flex;
    overflow: hidden;
    box-shadow: 0 6px 18px rgba(0,0,0,0.18);
  }
  .panel {
    position: relative;
    height: 100%;
    display: flex;
    flex-direction: column;
    align-items: center;
  }
  .panel--orange {
    width: 520px;
    background: var(--panel-orange);
    border-right: 2px solid var(--divider);
    padding-top: 120px;
  }
  .panel--white {
    flex: 1;
    background: var(--panel-white);
    padding-top: 70px;
    padding-right: 110px;
  }
  .brand-name {
    display: flex;
    align-items: center;
    gap: 12px;
    font-family: "Arimo", Arial, sans-serif;
    font-weight: 700;
    font-size: 34px;
    letter-spacing: 2px;
    text-transform: uppercase;
  }
  .brand-name__mark {
    width: 14px;
    height: 14px;
    border-radius: 50%;
    background: currentColor;
  }
  .panel--orange .brand-name { color: #ffffff; }
  .panel--white .brand-name { color: var(--ink); }
  .headline {
    margin-top: 44px;
    font-family: "Arimo", Arial, sans-serif;
    font-weight: 700;
    color: var(--ink);
    text-align: center;
    line-height: 0.95;
    text-transform: uppercase;
  }
  .headline__top { display: block; font-size: 66px; letter-spacing: 2px; }
  .headline__bottom { display: block; font-size: 94px; letter-spacing: 2px; }
  .panel--white .headline { margin-top: 56px; }
  .panel--white .headline__top { font-size: 76px; }
  .panel--white .headline__bottom { font-size: 108px; }
  .slogan {
    position: absolute;
    left: 190px;
    top: 478px;
    width: 620px;
    font-family: "Marcellus", Georgia, serif;
    font-size: 36px;
    letter-spacing: 1.5px;
    color: var(--ink);
    text-transform: uppercase;
    white-space: nowrap;
    text-align: center;
  }
  .pattern-strip {
    position: absolute;
    right: 0;
    top: 130px;
    width: 120px;
    height: 390px;
    background: linear-gradient(200deg, var(--pattern-light) 0%, var(--pattern-mid) 50%, var(--pattern-deep) 100%);
    opacity: 0.9;
  }
</style>
</head>
<body>
  <main class="billboard">
    <section class="panel panel--orange">
      <div class="brand-name"><span class="brand-name__mark"></span>Velvorn Casino</div>
      <h1 class="headline">
        <span class="headline__top">Coming</span>
        <span class="headline__bottom">Soon</span>
      </h1>
    </section>
    <section class="panel panel--white">
      <div class="brand-name"><span class="brand-name__mark"></span>Velvorn Casino</div>
      <h2 class="headline">
        <span class="headline__top">Coming</span>
        <span class="headline__bottom">Soon</span>
      </h2>
      <div class="pattern-strip" role="img" aria-label="Cascade of orange and red diamond shapes along the right edge"></div>
    </section>
    <p class="slogan">So many ways to have fun</p>
  </main>
</body>
</html>
```